Ecommerce Website For Printing Company

Zoravquill.com are a print, design and signage company who sell flyers, business cards, posters, brochures and more to customers in the UK.

Our website is outdated and requires a new design using current web styling and mobile functionality.

We require the following pages to be designed;
- Home Page
- Price Page
- Portfolio Page
- Blog
- Content Page

Our competitors in the printing industry are www.brenticade.com, www.hallowmarsh.co.uk, quorelvane.co.uk, www.tambridok.co.uk

We require the website to give a professional image as well as be easy for customers to navigate, understand and find prices.

Target Market(s)

Businesses

Industry/Entity Type

Printing

Number of Pages Required

4 page

Font styles to use
Sans Serif

Colors
33a6d7

Requirements
Must have
• Popular products, latest news/blog, sales from portfolio, newsletter sign up, footer

```html
<!DOCTYPE html>
<html lang="en">
<head>
<meta charset="utf-8">
<title>Zoravquill.com – Design Rates</title>
<link href="https://fonts.googleapis.com/css2?family=Open+Sans:wght@400;600;700&display=swap" rel="stylesheet">
<style>
:root{
  --brand:#33a6d7;
  --brand-dark:#1f86b4;
  --navy:#1b3f73;
  --page:#23282b;
  --panel:#2c3236;
  --panel-line:#3a4146;
  --white:#ffffff;
  --card:#f1f3f4;
  --text:#4a4f53;
  --muted:#8b9298;
  --green:#59b640;
  --foot-text:#c3c9cd;
}
*{box-sizing:border-box;margin:0;padding:0}
html,body{width:853px;height:1200px;overflow:hidden}
body{background:var(--page);font-family:"Open Sans",Arial,sans-serif;color:var(--text);position:relative}
a{color:inherit;text-decoration:none}

.utility-bar{position:absolute;top:0;left:0;width:853px;height:28px;background:#181c1e;font-size:8px;color:var(--foot-text);display:flex;align-items:center;justify-content:space-between;padding:0 51px}
.utility-bar .offer{color:var(--brand);font-weight:600;letter-spacing:.3px}
.utility-bar .links{display:flex;gap:18px}
.utility-bar .basket{color:var(--white)}

.site-header{position:absolute;top:28px;left:0;width:853px;height:80px;background:var(--white)}
.brand{position:absolute;left:51px;top:14px;display:flex;align-items:center;gap:8px;font-size:26px;font-weight:700;color:var(--navy)}
.brand .mark{width:14px;height:14px;background:var(--brand)}
.phone{position:absolute;right:23px;top:14px;font-size:16px;color:var(--brand);font-weight:600}
.main-nav{position:absolute;right:23px;top:44px;height:28px;background:var(--brand);display:flex;align-items:center;padding:0 14px;gap:16px;font-size:10px;color:var(--white);font-weight:600}
.main-nav .active{color:#dff3fb}
.main-nav svg{display:block}
.dropdown{position:absolute;left:530px;top:100px;width:96px;background:#2a2f33;font-size:8px;color:var(--white);z-index:3}
.dropdown li{list-style:none;padding:6px 9px;border-bottom:1px solid var(--panel-line)}
.dropdown li:first-child{background:var(--brand)}

.sidebar{position:absolute;left:51px;top:128px;width:262px}
.rate-menu{background:var(--panel);border:1px solid var(--panel-line);padding:10px 0 12px}
.rate-menu h3{font-size:14px;color:var(--white);font-weight:600;padding:4px 16px 10px;border-bottom:1px solid var(--panel-line)}
.rate-menu .group{font-size:12px;color:var(--brand);padding:9px 16px;border-bottom:1px solid var(--panel-line)}
.rate-menu ul{list-style:none;padding:6px 0}
.rate-menu li{font-size:9.5px;color:var(--foot-text);padding:4px 16px 4px 30px;position:relative}
.rate-menu li::before{content:"";position:absolute;left:18px;top:9px;width:4px;height:4px;background:var(--brand)}
.ad-slot{background:var(--white);margin-top:18px;padding:18px 24px;width:200px}
.ad-slot .art{width:152px;height:170px}

.content{position:absolute;left:341px;top:128px;width:489px;height:842px;background:var(--white);padding:22px 20px}
.hero{position:relative;height:140px;overflow:hidden}
.hero .art{position:absolute;inset:0;background:linear-gradient(100deg,#e9ecee 0%,#d8dde0 45%,#f6c9a0 62%,#e94f7a 72%,#7a5bd0 82%,#3aa0d8 92%,#9fd36b 100%)}
.hero h1{position:absolute;left:16px;top:22px;background:var(--brand);color:var(--white);font-size:17px;font-weight:700;padding:7px 14px;letter-spacing:.4px}
.intro{font-size:9px;line-height:1.55;margin-top:14px}
.vat{font-size:7.5px;color:#d9534f;text-align:right;margin-top:6px}
.rates{display:grid;grid-template-columns:repeat(3,1fr);gap:12px;margin-top:8px}
.rate-card{background:var(--card);height:90px;padding:9px 10px;position:relative}
.rate-card h4{font-size:9px;font-weight:600;color:var(--text);line-height:1.35}
.rate-card .price{position:absolute;left:10px;bottom:9px;font-size:22px;color:var(--brand);font-weight:400}
.shop-btn{position:absolute;right:9px;bottom:13px;background:var(--green);color:var(--white);font-size:7.5px;font-weight:700;padding:5px 8px;display:flex;align-items:center;gap:4px}

.newsletter{position:absolute;top:1003px;left:0;width:853px;height:42px;background:var(--brand);display:flex;align-items:center;padding:0 51px;gap:14px;color:var(--white)}
.newsletter h2{font-size:15px;font-weight:700;width:170px}
.newsletter .field{width:150px;height:20px;background:var(--white);font-size:7.5px;color:var(--muted);padding:5px 7px}
.newsletter label{font-size:8.5px;display:flex;align-items:center;gap:5px;margin-left:10px}
.newsletter label span{width:10px;height:10px;background:var(--white);display:inline-block}
.signup{margin-left:auto;background:var(--green);font-size:10px;font-weight:700;padding:5px 16px;width:130px;text-align:center}

.site-footer{position:absolute;top:1045px;left:0;width:853px;height:155px;text-align:center;color:var(--foot-text)}
.foot-links{display:flex;justify-content:center;gap:16px;font-size:9px;margin-top:18px}
.foot-links.second{margin-top:8px}
.social{display:flex;justify-content:center;gap:12px;margin-top:18px}
.social span{width:22px;height:22px;border-radius:50%;background:#50585e;display:block}
.legal{font-size:7px;line-height:1.5;color:var(--muted);margin:14px auto 0;width:520px}
</style>
</head>
<body>

<div class="utility-bar">
  <span class="offer">FREE SHIPPING ON ALL ORDERS</span>
  <div class="links"><span>Live chat</span><span>Support</span><span>Trade Account</span><span>Login</span><span class="basket">BASKET (£0.00)</span></div>
</div>

<header class="site-header">
  <div class="brand"><span class="mark"></span>Zoravquill.com</div>
  <div class="phone">Call us : 01632 960 418</div>
  <nav class="main-nav">
    <span>Home</span><span>About</span><span>Printing</span><span class="active">Graphic design</span><span>Website design</span><span>Artwork guide</span>
    <svg width="11" height="11" viewBox="0 0 12 12"><circle cx="5" cy="5" r="3.6" fill="none" stroke="#fff" stroke-width="1.6"/><line x1="7.6" y1="7.6" x2="11" y2="11" stroke="#fff" stroke-width="1.6"/></svg>
  </nav>
</header>
<ul class="dropdown"><li>Design Rates</li><li>Artwork Portfolio</li></ul>

<aside class="sidebar">
  <div class="rate-menu">
    <h3>ALL RATES</h3>
    <div class="group">Large Format</div>
    <div class="group">Popular Products</div>
    <ul>
      <li>Flyer Printing</li><li>Leaflet Printing</li><li>Brochure Printing</li><li>Poster Printing</li>
      <li>Business Cards</li><li>Letterhead Printing</li><li>Compliment Slips</li><li>Pullup Banners</li>
      <li>Invoice Pads &amp; NCR Pads</li><li>Stickers and Labels</li><li>Presentation Folders</li><li>Christmas Cards</li>
    </ul>
    <div class="group">Contact Prices</div>
  </div>
  <div class="ad-slot"><div class="art" role="img" aria-label="Advert for weekend getaway breaks" style="background:linear-gradient(180deg,#f5f7f2,#e6ecd9)"></div></div>
  <div class="ad-slot"><div class="art" role="img" aria-label="Advert for a print prize draw" style="background:linear-gradient(180deg,#eef3c8,#d6e08c)"></div></div>
</aside>

<main class="content">
  <div class="hero">
    <div class="art" role="img" aria-label="Designer's desk with colour swatch fan"></div>
    <h1>DESIGN RATES</h1>
  </div>
  <p class="intro">We don't believe in charging you by the hour and then giving you a big bill once the design is complete. All our design prices are agreed up front so you know the total cost before we start. We also offer unlimited amends free of charge on every project.</p>
  <p class="vat">* Prices exclude VAT</p>
  <section class="rates">
    <div class="rate-card"><h4>Single Sided Leaflet or Poster Design</h4><span class="price">£40</span><a class="shop-btn">› SHOP NOW</a></div>
    <div class="rate-card"><h4>Roll-up Banner Design (Text and Logo)</h4><span class="price">£25</span><a class="shop-btn">› SHOP NOW</a></div>
    <div class="rate-card"><h4>Double Sided Leaflet Design</h4><span class="price">£60</span><a class="shop-btn">› SHOP NOW</a></div>
    <div class="rate-card"><h4>Business Cards, Letterhead and Raffle Tickets</h4><span class="price">£20</span><a class="shop-btn">› SHOP NOW</a></div>
    <div class="rate-card"><h4>Roll-up Banner Design (Full Design)</h4><span class="price">£50</span><a class="shop-btn">› SHOP NOW</a></div>
    <div class="rate-card"><h4>Folded Leaflet Design (up to 6 panels)</h4><span class="price">£80</span><a class="shop-btn">› SHOP NOW</a></div>
    <div class="rate-card"><h4>Brochure Design (per page)</h4><span class="price">£20</span><a class="shop-btn">› SHOP NOW</a></div>
    <div class="rate-card"><h4>Logo Design</h4><span class="price">£75</span><a class="shop-btn">› SHOP NOW</a></div>
  </section>
</main>

<section class="newsletter">
  <h2>OUR NEWSLETTER</h2>
  <div class="field">Enter your e-mail here</div>
  <label><span></span>Offers</label>
  <label><span></span>Printing News</label>
  <label><span></span>All</label>
  <div class="signup">SIGN UP</div>
</section>

<footer class="site-footer">
  <div class="foot-links"><span>About</span><span>Printing</span><span>Graphic Design</span><span>Website Design</span><span>Artwork guide</span><span>Contact us</span><span>Testimonials</span><span>Blog</span><span>Contact us</span></div>
  <div class="foot-links second"><span>Special Offers</span><span>Terms and conditions</span><span>Privacy Policy</span><span>Trade Account</span></div>
  <div class="social"><span></span><span></span><span></span><span></span><span></span></div>
  <p class="legal">Registered in England and Wales, company number 00000000. Registered office: Unit 4, Harrow Works, Northgate, County Durham. All prices exclude VAT unless stated. © Zoravquill.com, all rights reserved.</p>
</footer>

</body>
</html>
```